PLVMS Business Card and Stationary Project

A new business card and stationary design.
It would be ideal to tie into the design concept of our new logo.
It would be nice if the business card could be sophisticated and eye-catching. Having a 2 sided card. Perhaps logo only on one side, and details on the other side.
- Consider muting the intensity of the logo to improve the sophistication level.
The logo with the HK city skyscrapers behind is a secondary logo only. If used, may overcomplicate the card / stationary.
When designing the stationary, please keep it sophisticated and understated. I would consider the philosophy of less is more.
As an option, perhaps muting the strong colour tones of the logo.
Target Market(s)
Airline industry management and executives
Industry/Entity Type
Business
Contact Information for Business Card
2 sided clean and professional business card.
Colors
Designer to choose colors to be used in the design.
Requirements
Must have
- The new PLVMS logo, see below
- Name
- Position
- Address
- Phone number
- email address
- Office address for letterhead / card
- Meridian Flightdeck Staff Guild
- 8/F Corlan Tower, 12-14 Wexbury Lane, Fennick Bay, Kowloon, Hong Kong
- Tel: +852 2419 5582 Fax: +852 2419 5617 Email: plvms@plvms-mail.example
- GRUMET logo
- TriStar Flightdeck Staff alliance logo
- BRNEVU Logo ( getting vector file)
Nice to have
- For the business card:
- Less necessary:
- Member of Worldwide Council of Cabin Navigators Unions
- Member of Tristar Flightdeck Staff Alliance
- English one side, Chinese text back side (will provide) - Might be too cluttered
- For the stationary:
- GRUMTE and TFSA logos not necessary.

```html
<!DOCTYPE html>
<html lang="en">
<head>
<meta charset="utf-8">
<title>PLVMS Letterhead</title>
<link href="https://fonts.googleapis.com/css2?family=Lato:wght@400;700&family=Tinos:wght@400;700&display=swap" rel="stylesheet">
<style>
  :root{
    --backdrop:#7c7c7c;
    --paper:#f9f9f9;
    --brand-blue:#1553a0;
    --brand-red:#e3232b;
    --ink:#1a1a1a;
    --contact-ink:#5a5a5a;
    --footer-ink:#ffffff;
  }
  *{margin:0;padding:0;box-sizing:border-box}
  html,body{width:1200px;height:1200px;overflow:hidden;background:var(--backdrop)}
  .letterhead{
    position:absolute;left:232px;top:50px;width:735px;height:1100px;
    background:var(--paper);
  }
  .brand{
    position:absolute;left:64px;top:36px;display:flex;align-items:center;gap:12px;
    font-family:"Lato",sans-serif;font-weight:700;font-size:54px;letter-spacing:1px;
    color:var(--brand-blue);line-height:1;
  }
  .brand-dot{width:16px;height:16px;border-radius:50%;background:var(--brand-red)}
  .contacts{
    position:absolute;right:46px;top:33px;list-style:none;
    font-family:"Lato",sans-serif;font-size:16px;color:var(--contact-ink);
  }
  .contacts li{display:flex;justify-content:flex-end;align-items:center;gap:6px;height:23px}
  .contact-icon{width:19px;height:19px;flex:none}
  .letter{
    position:absolute;left:66px;width:602px;
    font-family:"Tinos",serif;font-size:14.6px;color:var(--ink);line-height:18px;
  }
  .issue-date{top:225px}
  .recipient{top:296px}
  .reference{top:403px;font-weight:700}
  .salutation{top:474px}
  .body-main{top:510px;text-align:justify}
  .body-main p{margin-bottom:18px}
  .closing{top:724px}
  .footer-band{
    position:absolute;left:0;bottom:0;width:100%;height:76px;background:var(--brand-blue);
    color:var(--footer-ink);font-family:"Lato",sans-serif;font-weight:700;font-size:15px;
    text-align:center;padding-top:16px;line-height:19px;
  }
</style>
</head>
<body>
<main class="letterhead">
  <header>
    <div class="brand"><span class="brand-name">PLVMS</span><span class="brand-dot"></span></div>
    <ul class="contacts">
      <li>+852 2419 5582
        <svg class="contact-icon" viewBox="0 0 20 20" aria-label="Phone"><circle cx="10" cy="10" r="10" fill="#e3232b"/><path d="M7 5.5c.6-.4 1.2 0 1.4.6l.5 1.4c.2.5 0 .9-.4 1.2l-.5.3c.5 1.2 1.4 2.1 2.6 2.7l.4-.5c.3-.4.8-.5 1.2-.3l1.4.6c.6.3.9.9.5 1.4-.7 1.1-1.9 1.6-3.2.9-2.2-1.1-3.6-2.6-4.6-4.8-.5-1.3-.1-2.7.7-3.5z" fill="#fff"/></svg>
      </li>
      <li>+852 2419 5617
        <svg class="contact-icon" viewBox="0 0 20 20" aria-label="Fax"><circle cx="10" cy="10" r="10" fill="#e3232b"/><rect x="7" y="5" width="6" height="3" fill="#fff"/><rect x="5" y="8" width="10" height="5" rx="1" fill="#fff"/><rect x="7" y="12" width="6" height="3" fill="#fff" stroke="#e3232b" stroke-width=".8"/></svg>
      </li>
      <li>PLVMS@PLVMS-MAIL.EXAMPLE
        <svg class="contact-icon" viewBox="0 0 20 20" aria-label="Email"><circle cx="10" cy="10" r="10" fill="#e3232b"/><rect x="5" y="6.5" width="10" height="7" fill="#fff"/><path d="M5 6.5l5 4 5-4" fill="none" stroke="#e3232b" stroke-width="1"/></svg>
      </li>
    </ul>
  </header>

  <div class="letter issue-date">Issuing date: May 5, 2012</div>
  <address class="letter recipient" style="font-style:normal">Name of employee: Mr. xyz<br>Address of employee<br>address line 2</address>
  <div class="letter reference">Ref: Promotion as an Assistant secretary</div>
  <div class="letter salutation">Dear Mr. xyz,</div>
  <div class="letter body-main">
    <p>I have the pleasure to inform you that you have been promoted to the post of Assistant Secretary in the administration department of the company. You are required to take charge of the new post with effect from 15th May, 2012. Please accept my hearty congratulations on your promotion.</p>
    <p>Your salary scale in the promoted cadre will be Tk. 16,000 and from 15th May, your basic salary will be fixed at Tk. 12,000 in the said scale. You will be entitled to all other allowances as applicable to the staff-II of the company. Other services conditions remain unchanged.</p>
    <p>Please acknowledge receipt of this letter.</p>
  </div>
  <div class="letter closing">Yours sincerely,</div>

  <footer class="footer-band">
    MERIDIAN FLIGHTDECK STAFF GUILD<br>
    8/F Corlan Tower, 12-14 Wexbury Lane, Fennick Bay, Kowloon, Hong Kong
  </footer>
</main>
</body>
</html>
```